THE BRIGHT KITE SITTER - Temporary, On The Spot , Child Minding and Dog Walking Service

I am THE BRIGHT KITE SITTER. I am available for temporary on-the-spot bookings, for those times when parents need 1 or 2 hours to duck out to the supermarket but they can' t because their baby is taking a nap. Or maybe they have a 1 to 2 hour appointment where they can't take the kids and have no one to look after them. Or they may be they are at a luncheon and have to reluctantly tear themselves away to pick up the kids from school.
This is where I come to the rescue.
I can be hired for a minimum of 1 hour, or a maximum of 2 hours. I will come to them. Daytime and Evening rates apply. Maximum 3 children at one time.
I will entertain the children, do the odd job around the house, make delicious snacks and I can pickup children from school when necessary. I am also available to walk your beloved dog.
The Bright Kite Sitter is like no other nanny you will ever have - fun, reliable, super-tidy , and comes with impeccable references. Your life will become a whole lot easier with me in it!

I'd like a flyer that looks 'classy' as well as eye-catching. I'm 51 years old, but a 'very young' 51 so I'm also looking for a modern flyer.

Target Market(s)

Busy Mums and Dads and Guardians.

Industry/Entity Type

It Service

Requirements
Must have
• Maximum of 3 children at any 1 time.
Should not have
• Nasty pets!

```html
<!DOCTYPE html>
<html lang="en">
<head>
<meta charset="utf-8">
<title>The Bright Kite Sitter – Flyer</title>
<link href="https://fonts.googleapis.com/css2?family=Open+Sans:ital,wght@0,600;0,700;0,800;1,600;1,700;1,800&display=swap" rel="stylesheet">
<style>
:root{
  --pink:#e6197a;
  --navy:#1d2d6b;
  --blue:#2f8fdc;
  --blue-dark:#1b6fc0;
  --sky:#cfe8fb;
  --yellow:#ffe23a;
  --white:#ffffff;
}
*{box-sizing:border-box;margin:0;padding:0}
html,body{width:853px;height:1200px;overflow:hidden;background:var(--white)}
body{font-family:"Open Sans",Arial,sans-serif;color:var(--navy)}
.flyer{position:relative;width:853px;height:1200px;overflow:hidden;background:var(--white)}
.headline{position:absolute;left:22px;top:18px;color:var(--pink);font-weight:800;font-size:44px;letter-spacing:.5px;z-index:2}
.subline{position:absolute;left:22px;top:76px;color:var(--navy);font-weight:700;font-size:28px;z-index:2}
.children-photo{position:absolute;left:200px;top:128px;width:653px;height:300px;
  background:linear-gradient(135deg,#f4d9c4 0%,#e9b98f 35%,#b9d5ee 70%,#7fb3e0 100%);}
.limit-badge{position:absolute;left:14px;top:140px;width:150px;height:150px;border-radius:50%;
  background:var(--pink);border:6px solid var(--white);box-shadow:0 3px 8px rgba(0,0,0,.25);
  display:flex;flex-direction:column;align-items:center;justify-content:center;color:var(--white);
  font-weight:800;font-size:17px;line-height:1.15;text-align:center;z-index:3}
.limit-badge .dot{width:34px;height:34px;border-radius:50%;background:var(--white);margin-bottom:8px}
.brand-band{position:absolute;left:0;top:428px;width:853px;height:150px;
  background:linear-gradient(180deg,var(--blue) 0%,var(--blue-dark) 100%);
  display:flex;flex-direction:column;align-items:center;justify-content:center}
.brand-name{font-weight:800;font-size:52px;color:var(--yellow);letter-spacing:1px}
.abn{margin-top:6px;font-weight:700;font-size:20px;color:var(--white)}
.intro{position:absolute;left:30px;top:596px;width:793px;font-weight:700;
  font-size:19px;line-height:1.4;text-align:center;color:var(--blue-dark)}
.promise{position:absolute;left:30px;top:728px;width:793px;font-weight:600;font-style:italic;
  font-size:18px;line-height:1.42;text-align:center;color:var(--navy)}
.promise strong{font-weight:800}
.rates{position:absolute;left:28px;top:895px;width:797px;height:88px;display:flex;gap:10px}
.rates .day{flex:0 0 360px;background:var(--blue);color:var(--white);padding:10px 18px;
  font-weight:700;font-size:17px;line-height:1.4}
.rates .day b{font-weight:800}
.rates .travel{flex:1;background:var(--sky);color:var(--navy);padding:10px 18px;
  font-weight:700;font-size:16px;line-height:1.4}
.tabs{position:absolute;left:28px;top:995px;width:797px;height:205px;display:flex;
  border-top:2px dashed var(--navy)}
.tab{flex:1;border-right:2px dashed var(--navy);display:flex;align-items:center;justify-content:center;gap:2px}
.tab:first-child{border-left:2px dashed var(--navy)}
.tab span{writing-mode:vertical-rl;transform:rotate(180deg);color:var(--pink);white-space:nowrap}
.tab .tab-name{font-weight:700;font-size:11px;color:var(--navy)}
.tab .tab-phone{font-weight:800;font-size:21px}
</style>
</head>
<body>
<main class="flyer">
  <div class="children-photo" role="img" aria-label="Photo of three smiling young children lying together on a blue background"></div>
  <h1 class="headline">SHE HAS ARRIVED!</h1>
  <p class="subline">For temporary On-The-Spot bookings</p>
  <div class="limit-badge"><span class="dot"></span>MAXIMUM<br>3 CHILDREN</div>

  <section class="brand-band">
    <div class="brand-name">THE BRIGHT KITE SITTER</div>
    <div class="abn">ABN: 12 345 678 901</div>
  </section>

  <p class="intro">Need to go to the supermarket but can't because the baby's asleep?<br>
  Have an appointment but you can't go because you have the children?<br>
  Reluctantly have to tear yourself away from that luncheon because the children need to be picked up from school?</p>

  <p class="promise"><strong>The Bright Kite Sitter will come to you!</strong><br>
  She will entertain your children, do the odd job around the house, and make delicious snacks. She will also pickup children from school when necessary and walk your beloved dog. The Bright Kite Sitter is fun, reliable, and comes with impeccable references.<br>
  <strong>And she is here to make your life a whole lot easier!</strong></p>

  <section class="rates">
    <div class="day"><b>DAY RATES:</b><br>Minimum hire 1hr - $30.00<br>Maximum hire 2hrs - $55.00</div>
    <div class="travel">For areas over 10km and up to 20km from Kitefield, an additional $10 fee applies on the overall hire rate.</div>
  </section>

  <section class="tabs">
    <div class="tab"><span class="tab-name">THE BRIGHT KITE SITTER</span><span class="tab-phone">0412 345 678</span></div>
    <div class="tab"><span class="tab-name">THE BRIGHT KITE SITTER</span><span class="tab-phone">0412 345 678</span></div>
    <div class="tab"><span class="tab-name">THE BRIGHT KITE SITTER</span><span class="tab-phone">0412 345 678</span></div>
    <div class="tab"><span class="tab-name">THE BRIGHT KITE SITTER</span><span class="tab-phone">0412 345 678</span></div>
    <div class="tab"><span class="tab-name">THE BRIGHT KITE SITTER</span><span class="tab-phone">0412 345 678</span></div>
    <div class="tab"><span class="tab-name">THE BRIGHT KITE SITTER</span><span class="tab-phone">0412 345 678</span></div>
    <div class="tab"><span class="tab-name">THE BRIGHT KITE SITTER</span><span class="tab-phone">0412 345 678</span></div>
    <div class="tab"><span class="tab-name">THE BRIGHT KITE SITTER</span><span class="tab-phone">0412 345 678</span></div>
    <div class="tab"><span class="tab-name">THE BRIGHT KITE SITTER</span><span class="tab-phone">0412 345 678</span></div>
    <div class="tab"><span class="tab-name">THE BRIGHT KITE SITTER</span><span class="tab-phone">0412 345 678</span></div>
  </section>
</main>
</body>
</html>
```